Webdesign für die Korvelt GmbH
Zielgruppe
Beratung • Renovierung • Reparatur • Planung • Bau • Pflege • Wartung im Bereich der Haustechnik
Aufgabenstellung
Bilder nur von bildmoro oder von der Webseite des Kunden nutzen

```html
<!DOCTYPE html>
<html lang="de">
<head>
<meta charset="utf-8">
<title>Korvelt Heizung-Sanitär GmbH</title>
<link href="https://fonts.googleapis.com/css2?family=Open+Sans:ital,wght@0,400;0,600;0,700;1,400&family=Comfortaa:wght@400;700&display=swap" rel="stylesheet">
<style>
:root{
  --blue:#1a84cf;
  --blue-dark:#0f79c6;
  --tile-1:#1090db;
  --tile-2:#2eb1e8;
  --tile-3:#4cc7d6;
  --text:#333;
  --muted:#666;
  --bg-soft:#f7f7f7;
  --bg-band:#ececec;
  --white:#fff;
}
*{box-sizing:border-box;margin:0;padding:0}
html,body{width:1037px;height:1200px;overflow:hidden;background:var(--white)}
body{position:relative;font-family:'Open Sans',sans-serif;color:var(--text)}
.abs{position:absolute}
.topstrip{left:0;top:0;width:1037px;height:17px;background:#f4f4f4}
.contact-bar{left:0;width:1037px;height:67px;background:var(--white);display:flex;align-items:center;gap:19px;font-size:10px;color:var(--text)}
.contact-bar.header{top:17px;padding-left:188px;box-shadow:0 2px 4px rgba(0,0,0,.06)}
.contact-bar.footer{top:1143px;height:52px;padding-left:122px;border-top:1px solid #eee}
.contact-bar b{font-weight:700}
.contact-bar .mini{font-family:'Comfortaa',sans-serif;font-size:7px;color:#555;display:flex;align-items:center;gap:5px}
.social{width:7px;height:9px;background:#777}
.nav{left:0;top:85px;width:1037px;height:33px;background:var(--bg-soft);display:flex;align-items:center;padding-left:188px}
.nav .home{width:35px;height:33px;background:#ebebeb;display:flex;align-items:center;justify-content:center;margin-right:14px}
.nav a{font-size:7.6px;color:var(--blue);text-decoration:none;margin-right:14px;letter-spacing:.1px}
.hero{left:0;top:118px;width:1037px;height:273px;background:linear-gradient(90deg,#c99a74 0%,#b88a66 20%,#8f8b86 35%,#d9dcdd 55%,#b7bcbe 75%,#e8eaeb 100%)}
.hero svg{position:absolute;left:0;top:0}
.features{left:0;top:391px;width:1037px;height:44px;background:var(--bg-soft);border-bottom:1px solid #e2e2e2}
.features .div{position:absolute;top:0;width:1px;height:44px;background:#ddd}
.feature{position:absolute;top:12px;display:flex;gap:6px;align-items:flex-start}
.feature h3{font-family:'Comfortaa',sans-serif;font-weight:400;font-size:10.5px;color:#333;line-height:11px}
.feature p{font-size:7px;color:#666;line-height:8px}
.brand{left:179px;top:366px;width:169px;height:48px;background:var(--white);display:flex;align-items:center;justify-content:center;font-family:'Open Sans',sans-serif;font-weight:700;font-size:22px;color:var(--blue);letter-spacing:.5px}
.tiles{left:0;top:435px;width:1037px;height:183px;background:var(--bg-band)}
.tile{position:absolute;top:12px;width:186px;height:154px;display:flex;justify-content:center;padding-top:48px;font-family:'Comfortaa',sans-serif;font-size:27px;color:var(--white)}
.tile.waerme{left:204px;background:linear-gradient(135deg,#0e85d4,#12a2e6 60%,#0b88d8)}
.tile.wasser{left:426px;background:linear-gradient(135deg,#27a8e6,#38b6ec 50%,#26a6e2)}
.tile.luft{left:647px;background:linear-gradient(135deg,#45c4d8,#55ccd8 50%,#3fbfd3)}
.arrow{position:absolute;top:60px}
.welcome{left:204px;top:618px;font-size:19px;font-weight:700;color:var(--blue);line-height:24px}
.intro-band{left:0;top:641px;width:1037px;height:111px;background:var(--bg-soft)}
.intro{left:204px;top:655px;width:358px;font-size:10px;line-height:19.5px;text-align:justify;color:#444}
.experience{left:729px;top:656px;width:103px;height:81px;background:var(--blue-dark);color:var(--white);padding:4px 6px;font-size:10.5px;line-height:16px}
.experience em{font-size:12px;display:block;margin-bottom:6px;opacity:.9}
.partner{left:0;top:770px;width:1037px;text-align:center;font-family:'Comfortaa',sans-serif;font-size:10.5px;line-height:14.5px;color:#555}
.partner span{color:var(--blue);margin:0 4px}
.partner .plain{color:#555;margin:0}
.scene{left:0;top:816px;width:1037px;height:316px;background:linear-gradient(90deg,#e6e1da 0%,#c9a27a 35%,#b47a45 55%,#e9e4dd 75%,#f1eeea 100%)}
.form{left:205px;top:842px;width:300px;height:238px;background:rgba(255,255,255,.72);padding:0 9px}
.form label{position:absolute;left:11px;font-size:10px;color:#666}
.form label b{color:#444;font-weight:600}
.form .field{position:absolute;left:9px;width:276px;height:25px;background:var(--white);border:1px solid #3c7bd0}
.form .send{position:absolute;left:229px;top:198px;width:56px;height:25px;background:#2f74c3;color:var(--white);font-size:8.5px;font-weight:600;display:flex;align-items:center;justify-content:center}
</style>
</head>
<body>
<div class="abs topstrip"></div>

<header class="abs contact-bar header">
  <span>Korvelt <b>Heizung-Sanitär GmbH</b></span>
  <span>Lindenweg 14</span>
  <span>09471 Tannbach / Erzg.</span>
  <span class="social" aria-label="Social Media"></span>
  <span class="mini"><svg width="14" height="10" viewBox="0 0 14 10"><rect x=".5" y=".5" width="13" height="9" fill="none" stroke="#555"/><path d="M.5 .5 7 6 13.5 .5" fill="none" stroke="#555"/></svg>info@korvelt-gmbh.de</span>
  <span class="mini"><svg width="10" height="10" viewBox="0 0 10 10"><path d="M2 1 4 3 3 4.5Q4.5 6.5 5.5 7L7 6 9 8 7.5 9.5Q3 8 .5 2.5Z" fill="#555"/></svg>03700-5120-0</span>
</header>

<nav class="abs nav">
  <span class="home"><svg width="13" height="12" viewBox="0 0 13 12"><path d="M6.5 0 13 6H11V12H8V8H5V12H2V6H0Z" fill="#e02020"/></svg></span>
  <a>MENÜ1</a><a>MENÜ-ABC-TEXT-BEISPIEL</a><a>MENÜ-3-TEXT</a><a>MENÜ-TITEL-2-TEXT</a><a>MENÜ-4-TEXT</a><a>MENÜ-5-TEXT</a>
</nav>

<div class="abs hero" role="img" aria-label="Foto: lachende Frau mit nassem Haar links, modernes Bad mit freistehender Wanne rechts">
  <svg width="1037" height="273"><path d="M527 0Q480 170 315 273" fill="none" stroke="#fff" stroke-width="2"/></svg>
</div>

<section class="abs features">
  <span class="div" style="left:387px"></span>
  <span class="div" style="left:592px"></span>
  <div class="feature" style="left:418px"><svg width="16" height="16"><circle cx="8" cy="8" r="7.5" fill="#3bbf3b"/></svg><div><h3>Erfahrung in 3. Generation</h3><p>seit 01. Juni 1949</p></div></div>
  <div class="feature" style="left:627px"><svg width="17" height="16" viewBox="0 0 17 16"><path d="M8.5 0 11 5.5 17 6 12.5 10 14 16 8.5 13 3 16 4.5 10 0 6 6 5.5Z" fill="#f6b21a"/></svg><div><h3>Handwerksqualität</h3><p>fachgerechte Umsetzung Ihrer Wünsche</p></div></div>
</section>

<div class="abs brand">KORVELT</div>

<section class="abs tiles">
  <svg class="arrow" style="left:125px" width="48" height="58" viewBox="0 0 48 58"><path d="M46 2 6 29 46 56M46 12 20 29 46 46" fill="none" stroke="#2d8ee0" stroke-width="3" stroke-dasharray="1.5 2.5"/></svg>
  <div class="tile waerme">Wärme</div>
  <div class="tile wasser">Wasser</div>
  <div class="tile luft">Luft</div>
  <svg class="arrow" style="left:865px" width="48" height="58" viewBox="0 0 48 58"><path d="M2 2 42 29 2 56M2 12 28 29 2 46" fill="none" stroke="#2d8ee0" stroke-width="3" stroke-dasharray="1.5 2.5"/></svg>
</section>

<div class="abs intro-band"></div>
<h1 class="abs welcome">Herzlich Willkommen</h1>
<p class="abs intro">Wenn Sie einen zuverlässigen Partner für die Erledigung Ihrer Aufträge suchen, Wert auf Kreativität und Freundlichkeit legen, dann sind Sie bei uns an der richtigen Stelle. Vom ersten Beratungsgespräch bis zur Übergabe der fertiggestellten Leistung, sollten Sie, wie viele Kunden vor Ihnen, gute Erfahrungen mit uns machen.</p>
<aside class="abs experience"><em>Erfahrung</em>1949 - 2019<br>über <b>65 Jahre</b><br>Firma Korvelt</aside>

<p class="abs partner">Wir sind Ihr zuverlässiger Partner bei Arbeiten rund um<br><span>Wärme</span> <span>Wasser</span> <span>Luft</span> <span>Dach</span> <span class="plain">und</span> <span style="margin-left:2px">Service</span>.</p>

<section class="abs scene" role="img" aria-label="Foto: helles Badezimmer mit Holzwand, freistehender Wanne, Waschtisch und Pflanzen"></section>
<form class="abs form">
  <label style="top:12px">Ihr <b>Name</b></label><span class="field" style="top:27px"></span>
  <label style="top:55px">Ihre <b>Telefonnummer</b></label><span class="field" style="top:68px"></span>
  <label style="top:105px">Ihr <b>Anliegen</b></label><span class="field" style="top:119px"></span>
  <label style="top:148px">Ihre <b>Nachricht</b></label><span class="field" style="top:160px"></span>
  <span class="send">Senden</span>
</form>

<footer class="abs contact-bar footer">
  <span>Korvelt <b>Heizung-Sanitär GmbH</b></span>
  <span>Lindenweg 14</span>
  <span>09471 Tannbach / Erzg.</span>
  <span class="social" aria-label="Social Media"></span>
  <span class="mini"><svg width="14" height="10" viewBox="0 0 14 10"><rect x=".5" y=".5" width="13" height="9" fill="none" stroke="#555"/><path d="M.5 .5 7 6 13.5 .5" fill="none" stroke="#555"/></svg>info@korvelt-gmbh.de</span>
  <span class="mini"><svg width="10" height="10" viewBox="0 0 10 10"><path d="M2 1 4 3 3 4.5Q4.5 6.5 5.5 7L7 6 9 8 7.5 9.5Q3 8 .5 2.5Z" fill="#555"/></svg>03700-5120-0</span>
</footer>
</body>
</html>
```